Structural Engineering Business Card

Veltrow Drafts does residential house plans for clients in Central Florida. Would like simple but elegant business card that is appropriate for a house plan engineering company. Prefer black business card with black/white them but open to other shades of blue. I uploaded a sample card that I came across that looked good but please come up with your own creative designs.

Contact Information for Business Card

Name, Title, Phone, Email, Address, website

```html
<!DOCTYPE html>
<html lang="en">
<head>
<meta charset="utf-8">
<title>Veltrow Drafts – Business Card</title>
<link href="https://fonts.googleapis.com/css2?family=Montserrat:wght@400;500;800&display=swap" rel="stylesheet">
<style>
  :root {
    --canvas: #3a3a3a;
    --card-white: #ffffff;
    --card-black: #161616;
    --ink: #111111;
    --ink-soft: #333333;
    --rule: #bdbdbd;
    --paper: #ffffff;
    --blueprint-a: #2a2a2a;
    --blueprint-b: #141414;
  }
  * { box-sizing: border-box; margin: 0; padding: 0; }
  html, body { width: 1200px; height: 1200px; overflow: hidden; }
  body {
    background: var(--canvas);
    font-family: "Montserrat", sans-serif;
    position: relative;
  }
  .card {
    position: absolute;
    left: 215px;
    width: 770px;
    height: 440px;
    border-radius: 30px;
    overflow: hidden;
  }
  .card--front { top: 120px; background: var(--card-white); color: var(--ink); }
  .card--back { top: 620px; background: var(--card-black); color: var(--paper); }

  .wordmark {
    position: absolute;
    font-weight: 800;
    text-transform: uppercase;
    letter-spacing: 1px;
    line-height: 1;
    white-space: nowrap;
  }
  .card--front .wordmark { left: 150px; top: 70px; font-size: 56px; color: var(--ink); }

  .rule { position: absolute; height: 2px; background: var(--rule); }
  .rule--top { left: 150px; right: 60px; top: 170px; }
  .rule--name { left: 150px; width: 330px; top: 330px; }

  .holder { position: absolute; left: 150px; top: 240px; padding-left: 18px; border-left: 5px solid var(--ink-soft); }
  .holder__name { font-size: 36px; font-weight: 500; line-height: 1; }
  .holder__title { font-size: 18px; font-weight: 400; margin-top: 6px; letter-spacing: 1px; }

  .contact { position: absolute; list-style: none; font-size: 18px; color: var(--ink-soft); }
  .contact li { display: flex; align-items: flex-start; gap: 12px; margin-bottom: 8px; line-height: 1.15; }
  .contact svg { width: 20px; height: 20px; flex: none; fill: var(--ink-soft); margin-top: 1px; }
  .contact--personal { left: 170px; top: 350px; }
  .contact--company { left: 500px; top: 225px; }

  .blueprint {
    position: absolute;
    left: 90px; top: 0; width: 560px; height: 440px;
    background: radial-gradient(ellipse at 50% 50%, var(--blueprint-a), var(--blueprint-b) 75%);
  }
  .card--back .wordmark {
    left: 0; right: 0; top: 185px; text-align: center;
    font-size: 74px; color: var(--paper);
  }
</style>
</head>
<body>
  <section class="card card--front" aria-label="Business card front">
    <div class="wordmark">Veltrow Drafts</div>
    <div class="rule rule--top"></div>

    <div class="holder">
      <div class="holder__name">JOHN DOE</div>
      <div class="holder__title">POSITION</div>
    </div>
    <div class="rule rule--name"></div>

    <ul class="contact contact--personal">
      <li>
        <svg viewBox="0 0 24 24"><path d="M6.6 10.8a15.1 15.1 0 0 0 6.6 6.6l2.2-2.2c.3-.3.7-.4 1-.2 1.1.4 2.3.6 3.6.6.6 0 1 .4 1 1V20c0 .6-.4 1-1 1A17 17 0 0 1 3 4c0-.6.4-1 1-1h3.5c.6 0 1 .4 1 1 0 1.3.2 2.5.6 3.6.1.3 0 .7-.2 1z"/></svg>
        <span>(000) 000 0000</span>
      </li>
      <li>
        <svg viewBox="0 0 24 24"><path d="M2 5h20v14H2zm2 2v.5l8 5 8-5V7zm0 2.8V17h16V9.8l-8 5z"/></svg>
        <span>email@youremail.com</span>
      </li>
    </ul>

    <ul class="contact contact--company">
      <li>
        <svg viewBox="0 0 24 24"><path d="M12 2a10 10 0 1 0 0 20 10 10 0 0 0 0-20zm6.9 6h-3a15 15 0 0 0-1.3-3.9A8 8 0 0 1 18.9 8zM12 4c.8 1.2 1.5 2.5 1.9 4h-3.8c.4-1.5 1.1-2.8 1.9-4zM4.3 14a8 8 0 0 1 0-4h3.4a16 16 0 0 0 0 4zm.8 2h3a15 15 0 0 0 1.3 3.9A8 8 0 0 1 5.1 16zm3-8h-3a8 8 0 0 1 4.3-3.9C8.8 5.3 8.4 6.6 8.1 8zM12 20c-.8-1.2-1.5-2.5-1.9-4h3.8c-.4 1.5-1.1 2.8-1.9 4zm2.3-6H9.7a14 14 0 0 1 0-4h4.6a14 14 0 0 1 0 4zm.3 5.9c.6-1.2 1-2.5 1.3-3.9h3a8 8 0 0 1-4.3 3.9zm1.7-5.9a16 16 0 0 0 0-4h3.4a8 8 0 0 1 0 4z"/></svg>
        <span>www.yourwebsite.com</span>
      </li>
      <li>
        <svg viewBox="0 0 24 24"><path d="M12 2a7 7 0 0 0-7 7c0 5.2 7 13 7 13s7-7.8 7-13a7 7 0 0 0-7-7zm0 9.5A2.5 2.5 0 1 1 12 6.5a2.5 2.5 0 0 1 0 5z"/></svg>
        <span>Your City Address 0000<br>Street Name, State, Country</span>
      </li>
    </ul>
  </section>

  <section class="card card--back" aria-label="Business card back">
    <div class="blueprint" role="img" aria-label="Faint architectural line drawing of a two-storey house elevation with dimension lines"></div>
    <div class="wordmark">Veltrow Drafts</div>
  </section>
</body>
</html>
```